Restaurant needs a vertical banner for fried catfish

Our restaurant is looking for an eye-catching 78.75in. x 36in. vertical physical banner ad for our fried catfish. Photos for the fried catfish will be provided as a reference but we will also accept anything similar to the photo. We will be using the following as our receptacle: https://www.plankoria.example/banner-stand/retractable-banner-stands/
The design must incorporate the following flavor texts:
Fried Catfish
Always Fresh!
Made from Scratch
Hand-cut Fillets
The Best Catfish in Texas
Served with fries, hush puppies, and a 32oz fountain drink
Also available by the pound!
The final design should be creative, professional, and eye-catching for customers.
Updates
Colors
Designer to choose colors to be used in the design.
Requirements
Must have
- We are open to any and all design elements, albeit the 'flavor texts' should not overpower, but complement the fried catfish photo. 'Fried Catfish' can be used in lieu of a main title/logo.
Nice to have
- Transparent or textured backgrounds that can encompass any or all part of the banner such as a cutting board, shadows, abstract, etc to show depth are a plus.
- Use of vectors or objects such as ribbons or shapes to encapsulate the 'flavor texts' are also encouraged.

```html
<!DOCTYPE html>
<html lang="en">
<head>
<meta charset="utf-8">
<title>Fried Catfish Banner</title>
<link rel="stylesheet" href="https://fonts.googleapis.com/css2?family=Alfa+Slab+One&family=Alegreya:wght@800&family=PT+Sans+Narrow:wght@700&family=Source+Sans+3:wght@600;700&display=swap">
<style>
  :root {
    --page: #ffffff;
    --ink-dark: #1c1a14;
    --tan: #a38b5c;
    --tan-deep: #8f7850;
    --cream: #f6eecb;
    --cream-edge: #efe3b4;
    --dot: #e8d982;
    --white: #ffffff;
    --title-top: #ffe640;
    --title-mid: #f7b51c;
    --title-low: #ef5a1c;
    --title-edge: #4a1d0a;
    --fillet: #c98a32;
    --fillet-light: #e0a948;
    --plate: #eeece6;
    --wood-dark: #141210;
    --wood: #2e2820;
  }
  html, body {
    margin: 0;
    width: 1200px;
    height: 1000px;
    overflow: hidden;
    background: var(--page);
  }
  .canvas {
    position: relative;
    width: 1200px;
    height: 1000px;
  }
  .banner {
    position: absolute;
    left: 403px;
    top: 68px;
    width: 394px;
    height: 864px;
    overflow: hidden;
    background: var(--ink-dark);
  }
  .doodle-backdrop {
    position: absolute;
    inset: 0;
    background:
      radial-gradient(circle at 20% 10%, rgba(214,170,70,.6), transparent 40%),
      radial-gradient(circle at 85% 12%, rgba(230,120,90,.5), transparent 35%),
      radial-gradient(circle at 15% 80%, rgba(120,150,60,.55), transparent 40%),
      radial-gradient(circle at 85% 88%, rgba(220,130,50,.55), transparent 40%),
      linear-gradient(180deg, #3a2c18, #241c12);
  }
  .title {
    position: absolute;
    left: 0;
    width: 100%;
    top: 26px;
    margin: 0;
    text-align: center;
    font-family: "Alfa Slab One", serif;
    font-weight: 400;
    line-height: .92;
  }
  .title span {
    display: block;
    -webkit-text-stroke: 2px var(--title-edge);
    -webkit-background-clip: text;
    background-clip: text;
    color: transparent;
  }
  .title .word-fried {
    font-size: 62px;
    background-image: linear-gradient(180deg, var(--title-top) 45%, var(--title-mid));
  }
  .title .word-catfish {
    font-size: 58px;
    background-image: linear-gradient(180deg, var(--title-mid), var(--title-low) 55%);
  }
  .band {
    position: absolute;
    left: 0;
    width: 100%;
    background: var(--tan);
    display: flex;
    align-items: center;
    justify-content: center;
    color: var(--white);
    z-index: 3;
  }
  .band .dot {
    position: absolute;
    top: 50%;
    width: 18px;
    height: 18px;
    margin-top: -9px;
    border-radius: 50%;
    background: var(--dot);
  }
  .band-fresh {
    top: 166px;
    height: 59px;
    font-family: "Source Sans 3", sans-serif;
    font-weight: 700;
    font-size: 30px;
  }
  .band-best {
    top: 642px;
    height: 52px;
    font-family: "Alegreya", serif;
    font-weight: 800;
    font-size: 23px;
  }
  .plate-photo {
    position: absolute;
    left: 0;
    top: 225px;
    width: 100%;
    height: 322px;
    background:
      radial-gradient(ellipse 30% 20% at 47% 55%, var(--fillet-light) 0%, var(--fillet) 45%, rgba(201,138,50,0) 100%),
      radial-gradient(ellipse 50% 30% at 50% 58%, var(--plate) 0%, rgba(238,236,230,.75) 55%, rgba(238,236,230,0) 100%),
      radial-gradient(ellipse 70% 60% at 50% 55%, var(--wood) 0%, var(--wood-dark) 100%);
  }
  .seal {
    position: absolute;
    left: 72px;
    top: 542px;
    width: 250px;
    height: 250px;
    border-radius: 50%;
    background: var(--cream);
    box-shadow: 0 0 0 3px var(--cream-edge), 0 0 0 5px var(--tan);
    z-index: 2;
    text-align: center;
    color: var(--tan-deep);
  }
  .seal-dots {
    position: absolute;
    top: 20px;
    left: 0;
    width: 100%;
  }
  .seal-text-top {
    position: absolute;
    top: 40px;
    width: 100%;
    margin: 0;
    font-family: "PT Sans Narrow", sans-serif;
    font-weight: 700;
    font-size: 18px;
    line-height: 24px;
    text-transform: uppercase;
  }
  .seal-serving {
    position: absolute;
    top: 162px;
    width: 100%;
    margin: 0;
    font-family: "PT Sans Narrow", sans-serif;
    font-weight: 700;
    font-size: 14px;
    line-height: 17px;
  }
  .seal-note {
    position: absolute;
    top: 207px;
    width: 100%;
    margin: 0;
    font-family: "PT Sans Narrow", sans-serif;
    font-weight: 700;
    font-size: 10px;
  }
</style>
</head>
<body>
<div class="canvas">
  <div class="banner">
    <div class="doodle-backdrop" role="img" aria-label="Colourful hand-drawn food doodle pattern in orange, yellow and green on black"></div>

    <h1 class="title">
      <span class="word-fried">FRIED</span>
      <span class="word-catfish">CATFISH</span>
    </h1>

    <div class="band band-fresh">
      <span class="dot" style="left:25px"></span>
      <span class="dot" style="left:53px"></span>
      Always Fresh!
      <span class="dot" style="right:53px"></span>
      <span class="dot" style="right:25px"></span>
    </div>

    <div class="plate-photo" role="img" aria-label="Photo of golden fried catfish fillets with fries, hush puppies and tartar sauce on a white plate on a dark wooden table"></div>

    <div class="seal">
      <svg class="seal-dots" width="250" height="12" viewBox="0 0 250 12">
        <circle cx="107" cy="6" r="4.5" fill="#d9cc9c"/>
        <circle cx="125" cy="6" r="6" fill="#d9cc9c"/>
        <circle cx="144" cy="6" r="4.5" fill="#d9cc9c"/>
      </svg>
      <p class="seal-text-top">Made from Scratch<br>Hand-cut Fillets</p>
      <p class="seal-serving">Served with fries, hush puppies,<br>and a 32oz fountain drink</p>
      <p class="seal-note">Also available by the pound!</p>
    </div>

    <div class="band band-best">
      <span class="dot" style="left:25px"></span>
      The Best Catfish in Texas
      <span class="dot" style="right:25px"></span>
    </div>
  </div>
</div>
</body>
</html>
```